Business Card Design Project

We need a business card designed for a new Luxury Custom Homebuilding company based in Arizona. We previous were called "Belcrest Estates" but want to start using "Belcrest Custom Homes" We want the message to communicate high end, luxury and cutting-edge. We like the blue, white and black color scheme.
Belcrest Custom Homes
Marcus T. Halloway
Chief Executive Officer
Office: 480-555-0142
Mobile: 480-555-0178
email: marc@belcrestcustom-example.com
web adress: www.BelcrestCustom-example.com
Updates
We have made a change to our website address and email address based on recieving feedback from a nmber of individuals. The feedback was web address and email address was to long. Therefore we have made a change. The new web adress and email adress are the following.
www.BelcrestCustom-example.com
marc@belcrestcustom-example.com
Also I decided against using in yellow. I like the colors blue,black, white and maybe gray.
Target Market(s)
Our target market is the wealthy individuals looking for a luxury high-end custom home.
Industry/Entity Type
Business
Look and feel

```html
<!DOCTYPE html>
<html lang="en">
<head>
<meta charset="utf-8">
<title>Belcrest Custom Homes – Business Card</title>
<link rel="stylesheet" href="https://fonts.googleapis.com/css2?family=Francois+One&family=Mulish:wght@600&display=swap">
<style>
  :root {
    --ink-black: #0b0c0d;
    --charcoal: #25282b;
    --band-deep: #0a22d8;
    --band-bright: #6f8dff;
    --glow-white: #ffffff;
    --sky-blue: #5ab8ea;
  }
  * { margin: 0; padding: 0; box-sizing: border-box; }
  html, body {
    width: 1200px;
    height: 720px;
    overflow: hidden;
    background: var(--ink-black);
  }
  .card {
    position: relative;
    width: 1200px;
    height: 720px;
    overflow: hidden;
    background: radial-gradient(ellipse 70% 60% at 50% 35%, var(--charcoal) 0%, #15171a 45%, var(--ink-black) 100%);
  }
  .header-band {
    position: absolute;
    inset: 0 0 auto 0;
    width: 1200px;
    height: 260px;
  }
  .tagline {
    font-family: "Francois One", "Arial Narrow", sans-serif;
    font-size: 58px;
    fill: var(--glow-white);
    filter: drop-shadow(0 0 6px rgba(255,255,255,0.9)) drop-shadow(0 0 14px rgba(160,190,255,0.8));
  }
  .skyline-art {
    position: absolute;
    left: 335px;
    top: 246px;
    width: 547px;
    height: 96px;
    background: linear-gradient(180deg, rgba(90,184,234,0) 0%, rgba(90,184,234,0.18) 70%, rgba(90,184,234,0.35) 100%);
  }
  .contact {
    position: absolute;
    left: 0;
    top: 380px;
    width: 1200px;
    list-style: none;
    text-align: center;
    font-family: "Mulish", Arial, sans-serif;
    font-weight: 600;
    font-size: 24px;
    line-height: 40.6px;
    color: var(--sky-blue);
  }
</style>
</head>
<body>
  <main class="card">
    <svg class="header-band" viewBox="0 0 1200 260" aria-hidden="false">
      <defs>
        <radialGradient id="bandGlow" cx="600" cy="175" r="620" gradientUnits="userSpaceOnUse">
          <stop offset="0" stop-color="var(--band-bright)"/>
          <stop offset="0.45" stop-color="#3c5cf5"/>
          <stop offset="1" stop-color="var(--band-deep)"/>
        </radialGradient>
        <path id="taglineCurve" d="M 200 106 Q 605 162 1010 108"/>
      </defs>
      <path class="band-fill" d="M0 0 H1200 V86 Q600 240 0 86 Z" fill="url(#bandGlow)"/>
      <path class="band-edge" d="M0 86 Q600 240 1200 86" fill="none" stroke="#b9c8ff" stroke-width="3" opacity="0.8"/>
      <text class="tagline" text-anchor="middle">
        <textPath href="#taglineCurve" startOffset="50%">Luxury Custom Homebuilding</textPath>
      </text>
    </svg>

    <div class="skyline-art" role="img" aria-label="Thin light-blue line drawing of a city skyline"></div>

    <ul class="contact">
      <li class="company">Belcrest Custom Homes</li>
      <li class="name">Marcus T. Halloway</li>
      <li class="title">Chief Executive Officer</li>
      <li class="office">Office: 480-555-0142</li>
      <li class="mobile">Mobile: 480-555-0178</li>
      <li class="email">email: marc@belcrestcustom-example.com</li>
      <li class="web">web adress: www.BelcrestCustom-example.com</li>
    </ul>
  </main>
</body>
</html>
```